Cedar Row Maintenance and Concierge Flyer

We need a flyer for cedar row maintenance and concierge service. We specialize in and provide residential maintenance and errand services to retired and semi retired persons living in the Lake Norman area. The services we include:
Lighting and plumbing repairs
Ceiling fan installation
Handicap accessories
Locks and security
Picture hanging
Hang blinds
Furniture arrangement / assembly
Pressure washing
Battery Jump start
and more...

Our Concierge services include:
Errand running
Grocery shopping
Wellness Checks
Dog Walk
Garbage Collection
and more...

We offer monthly service agreements and 24/7 access
Call text or e-mail for more information
704.555.0187
1cedarrowmaint@quillpostmail.com

The design should invoke a sense of trust and a customer service driven mission

Target Market(s)

Residential maintenance

Industry/Entity Type

Property Maintenance

Contact Information for Business Card

Derek Halvorsen
48176 Quimby Ferrel Rd.
Cornelius NC 28031
704.555.0187
with uploaded logo

Requirements
Nice to have
• Would like a postcard size flyer. Front and back
Should not have
• No pics of of people wearing hard hats or pics of blueprints. No pics of commercial or industrial maintenance.

```html
<!DOCTYPE html>
<html lang="en">
<head>
<meta charset="utf-8">
<title>Cedar Row Maintenance &amp; Concierge – Business Card</title>
<link rel="stylesheet" href="https://fonts.googleapis.com/css2?family=Source+Sans+3:wght@400;600&display=swap">
<style>
  :root {
    --backdrop: #9c9da0;
    --card-front: #f1f1f3;
    --card-back: #6f7175;
    --ink: #5f6165;
    --ink-soft: #6a6c70;
    --accent: #b8191c;
    --band-gray: #7d7f83;
    --back-text: #eceef0;
    --back-mark: rgba(255, 255, 255, 0.07);
  }
  * { margin: 0; padding: 0; box-sizing: border-box; }
  html, body {
    width: 1105px; height: 1200px; overflow: hidden;
    background: var(--backdrop);
    font-family: "Source Sans 3", "Segoe UI", sans-serif;
  }
  .card {
    position: absolute; left: 180px; width: 746px; height: 425px; overflow: hidden;
  }
  /* Front */
  .card-front { top: 120px; background: var(--card-front); }
  .brand {
    position: absolute; left: 55px; top: 48px;
    display: flex; align-items: center; gap: 18px;
  }
  .brand-dot {
    width: 74px; height: 74px; border-radius: 50%; background: var(--accent);
  }
  .brand-name {
    color: var(--ink); font-weight: 400; font-size: 34px; line-height: 1.1;
  }
  .contact-list {
    position: absolute; left: 55px; top: 282px; list-style: none;
  }
  .contact-list li {
    display: flex; align-items: center; gap: 10px;
    font-size: 20px; color: var(--ink); height: 29px;
  }
  .contact-list svg { width: 17px; height: 17px; fill: var(--ink-soft); flex: none; }
  .person {
    position: absolute; right: 55px; top: 295px; text-align: right;
  }
  .person-name {
    font-size: 25px; font-weight: 600; color: var(--ink-soft); letter-spacing: 0.5px;
  }
  .person-title { font-size: 20px; color: var(--accent); margin-top: 2px; }
  .footer-band { position: absolute; left: 0; bottom: 0; width: 746px; height: 18px; }
  /* Back */
  .card-back { top: 635px; background: var(--card-back); }
  .back-mark {
    position: absolute; left: 375px; top: 37px;
    width: 340px; height: 340px; border-radius: 50%; background: var(--back-mark);
  }
  .services { position: absolute; left: 44px; top: 44px; color: var(--back-text); }
  .services-title { font-size: 27px; font-weight: 600; margin-bottom: 6px; }
  .services-list { list-style: none; }
  .services-list li {
    font-size: 20px; height: 34px; line-height: 34px; padding-left: 24px; position: relative;
  }
  .services-list li::before {
    content: ""; position: absolute; left: 4px; top: 15px;
    width: 6px; height: 6px; border-radius: 50%; background: var(--back-text);
  }
</style>
</head>
<body>
  <section class="card card-front">
    <div class="brand">
      <span class="brand-dot"></span>
      <span class="brand-name">Cedar Row<br>Maintenance &amp; Concierge</span>
    </div>

    <ul class="contact-list">
      <li>
        <svg viewBox="0 0 24 24" aria-hidden="true"><path d="M6.6 10.8a15.1 15.1 0 0 0 6.6 6.6l2.2-2.2a1 1 0 0 1 1-.25 11.4 11.4 0 0 0 3.6.57 1 1 0 0 1 1 1V20a1 1 0 0 1-1 1A17 17 0 0 1 3 4a1 1 0 0 1 1-1h3.5a1 1 0 0 1 1 1c0 1.25.2 2.45.57 3.57a1 1 0 0 1-.25 1z"/></svg>
        704.555.0187
      </li>
      <li>
        <svg viewBox="0 0 24 24" aria-hidden="true"><path d="M2 5h20v14H2z" opacity=".9"/><path d="M2 5l10 8 10-8" fill="none" stroke="#f1f1f3" stroke-width="1.8"/></svg>
        1cedarrowmaint@quillpostmail.com
      </li>
      <li>
        <svg viewBox="0 0 24 24" aria-hidden="true"><circle cx="12" cy="12" r="10"/><path d="M2 12h20M12 2c3 3 3 17 0 20M12 2c-3 3-3 17 0 20" fill="none" stroke="#f1f1f3" stroke-width="1.4"/></svg>
        www.1cedarrowmaint.com
      </li>
    </ul>

    <div class="person">
      <p class="person-name">DEREK HALVORSEN</p>
      <p class="person-title">CEO/Founder</p>
    </div>

    <svg class="footer-band" viewBox="0 0 746 18" aria-hidden="true">
      <polygon points="0,0 487,0 483,18 0,18" fill="var(--band-gray)"/>
      <polygon points="491,0 746,0 746,18 487,18" fill="var(--accent)"/>
    </svg>
  </section>

  <section class="card card-back">
    <span class="back-mark"></span>
    <div class="services">
      <h2 class="services-title">Services:</h2>
      <ul class="services-list">
        <li>Lighting &amp; plumbing repairs</li>
        <li>Ceiling fan installation</li>
        <li>Handicap accessories</li>
        <li>Locks &amp; security</li>
        <li>Picture hanging</li>
        <li>Hang blinds</li>
        <li>Furniture arrangement / assembly</li>
        <li>Pressure washing</li>
        <li>Battery Jump start &amp; more...</li>
      </ul>
    </div>
  </section>
</body>
</html>
```